Marlow Crest Group (Real Estate and Investment)

A high end, clean design.
We are a real estate company with sales, asset management and investment divisions. We want to use a black and white scheme which is really high end feel. The back of the card can just be the logo (black background with the white writing) as we will probably emboss this when we print)

Target Market(s)

High level investors, high end houses for sale

Industry/Entity Type

Business

Contact Information for Business Card

Name, position, phone number and email address
Glen Varley, Managing Director, 0437259064 and glen@marlowcrest-example.com.au

Requirements
Must have
• Back of the card to be the black background with the white writing (as per the attached images). Would like the capacity to emboss the writing and logo

```html
<!DOCTYPE html>
<html lang="en">
<head>
<meta charset="utf-8">
<title>Marlow Crest Group — Business Card</title>
<link rel="stylesheet" href="https://fonts.googleapis.com/css2?family=Raleway:wght@300;400;600&display=swap">
<style>
  :root {
    --backdrop: #8f9a99;
    --card-white: #ffffff;
    --card-black: #2f2f2f;
    --ink: #1c1c1c;
    --ink-soft: #555555;
    --rule: #9a9a9a;
    --frame: #6a6a6a;
    --skyline-top: #ffffff;
    --skyline-bottom: #e4e6e6;
  }
  * { box-sizing: border-box; margin: 0; padding: 0; }
  html, body {
    width: 1200px;
    height: 899px;
    overflow: hidden;
  }
  body {
    background: var(--backdrop);
    font-family: "Raleway", sans-serif;
    position: relative;
  }

  .card {
    position: absolute;
    top: 180px;
    width: 300px;
    height: 525px;
    background: var(--card-white);
    box-shadow: 0 14px 30px rgba(0, 0, 0, 0.25);
  }
  .card--back { left: 260px; padding: 16px; }
  .card--front { left: 640px; padding: 12px; }

  /* Back of card */
  .back-panel {
    width: 100%;
    height: 100%;
    background: var(--card-black);
    border-radius: 24px;
    display: flex;
    flex-direction: column;
    align-items: center;
    justify-content: center;
    gap: 20px;
    padding: 0 30px 40px;
    color: var(--card-white);
  }
  .back-mark {
    width: 60px;
    height: 60px;
    border: 2px solid var(--card-white);
    border-radius: 50%;
  }
  .back-wordmark {
    font-weight: 300;
    font-size: 17px;
    letter-spacing: 0.04em;
    text-transform: uppercase;
    text-align: center;
    white-space: nowrap;
    line-height: 1.3;
  }

  /* Front of card */
  .front-frame {
    position: relative;
    width: 100%;
    height: 100%;
    border: 1px solid var(--frame);
    border-radius: 14px;
    display: flex;
    flex-direction: column;
    align-items: center;
    padding-top: 58px;
    overflow: hidden;
    color: var(--ink);
  }
  .front-mark {
    width: 56px;
    height: 56px;
    border: 1.5px solid var(--ink);
    border-radius: 50%;
  }
  .person-name {
    margin-top: 22px;
    font-weight: 600;
    font-size: 23px;
    letter-spacing: 0.04em;
    text-transform: uppercase;
    white-space: nowrap;
  }
  .person-role {
    margin-top: 8px;
    font-weight: 400;
    font-size: 11px;
    color: var(--ink-soft);
  }
  .contact-list {
    list-style: none;
    margin-top: 48px;
    width: 160px;
    text-align: center;
  }
  .contact-item {
    font-weight: 400;
    color: var(--ink-soft);
    padding-bottom: 6px;
    border-bottom: 2px solid var(--rule);
    margin-bottom: 14px;
  }
  .contact-item--phone { font-size: 15px; letter-spacing: 0.08em; }
  .contact-item--email { font-size: 8px; white-space: nowrap; }
  .skyline {
    position: absolute;
    left: 0;
    right: 0;
    bottom: 0;
    height: 90px;
    background: linear-gradient(to bottom, var(--skyline-top), var(--skyline-bottom));
  }
</style>
</head>
<body>
  <section class="card card--back" aria-label="Card back">
    <div class="back-panel">
      <div class="back-mark"></div>
      <p class="back-wordmark">Marlow Crest Group</p>
    </div>
  </section>

  <section class="card card--front" aria-label="Card front">
    <div class="front-frame">
      <div class="front-mark"></div>
      <h1 class="person-name">Glen Varley</h1>
      <p class="person-role">Managing Director</p>
      <ul class="contact-list">
        <li class="contact-item contact-item--phone">0437259064</li>
        <li class="contact-item contact-item--email">glen@marlowcrest-example.com.au</li>
      </ul>
      <div class="skyline" role="img" aria-label="Faint line drawing of a city skyline along the bottom edge"></div>
    </div>
  </section>
</body>
</html>
```